Cutting edge/Modern brochure for #1 Indie real estate brokerage in the area.

Professional/Modern looking marketing brochures that we can leave behind after a listing or buyer presentation. We are the #1 local Indie Real Estate Company and a group of top producing agents broke away from the corporate real estate world. We just opened our second location which is 6,000 sq ft and a very modern design. Our website is www.brevanhomes.com and our facebook page Brevan Homes Real Estate Services has a sneak peak commercial of the new office to get inspiration. Attached is a file with verbiage and our logo with a black background and one with no background. We have cutting edge technology, offer 3D spacevue technology with virtual tours, radio show, etc...We want these pieces to be powerful to make the clients want to choose us!

Target Market(s)

We would like a brochure for buyers and one for sellers

Industry/Entity Type

Real Estate

Colors

Designer to choose colors to be used in the design.

Requirements
Must have
• Sleek, modern, professional look

```html
<!DOCTYPE html>
<html lang="en">
<head>
<meta charset="utf-8">
<title>Brevan Homes – Brochure Cover Spread</title>
<link rel="stylesheet" href="https://fonts.googleapis.com/css2?family=Roboto:wght@400;700;900&display=swap">
<style>
  :root {
    --stage: #9a9a9c;
    --paper-light: #e3e3e8;
    --paper-band: #d2d2d8;
    --ink-dark: #2a2a2c;
    --ink-text: #1f1f22;
    --gold: #d9c23a;
    --gold-deep: #b89a1f;
    --white: #ffffff;
    --photo-light-a: #c9c9d0;
    --photo-light-b: #8a8a96;
    --photo-dark-a: #d8d8d8;
    --photo-dark-b: #5d6066;
  }
  * { margin: 0; padding: 0; box-sizing: border-box; }
  html, body { width: 1200px; height: 789px; overflow: hidden; }
  body {
    background: var(--stage);
    font-family: "Roboto", Arial, sans-serif;
    position: relative;
  }
  .spread {
    position: absolute;
    left: 160px; top: 94px;
    width: 880px; height: 600px;
    display: flex;
    box-shadow: 0 14px 30px rgba(0,0,0,0.25);
  }
  .page {
    position: relative;
    width: 440px; height: 600px;
    overflow: hidden;
  }
  .page svg.page-art { position: absolute; inset: 0; }

  /* back cover */
  .back-cover { background: var(--paper-light); }
  .back-cover .tagline {
    position: absolute;
    left: 0; right: 0; top: 498px;
    text-align: center;
    font-weight: 900;
    font-size: 19px;
    letter-spacing: 0.2px;
    color: var(--ink-text);
    text-transform: uppercase;
  }
  .web-link {
    position: absolute;
    display: flex; align-items: center; gap: 8px;
    font-size: 14px;
    letter-spacing: 0.3px;
  }
  .back-cover .web-link {
    left: 0; right: 0; top: 534px;
    justify-content: center;
    color: var(--ink-text);
  }

  /* front cover */
  .front-cover { background: var(--ink-dark); }
  .headline-rank {
    position: absolute;
    left: 50px; top: 44px;
    display: flex; align-items: center; gap: 10px;
  }
  .rank-number {
    font-weight: 900;
    font-size: 74px;
    line-height: 1;
    color: var(--gold);
    letter-spacing: -2px;
  }
  .rank-label {
    font-weight: 700;
    font-size: 15px;
    line-height: 1.15;
    color: var(--white);
    text-transform: uppercase;
  }
  .brand-name {
    position: absolute;
    right: 26px; top: 70px;
    display: flex; align-items: center; gap: 8px;
    font-weight: 700;
    font-size: 15px;
    letter-spacing: 1px;
    color: var(--gold);
    text-transform: uppercase;
  }
  .brand-mark {
    width: 12px; height: 12px;
    background: var(--gold);
  }
  .announcement {
    position: absolute;
    left: 56px; top: 452px;
    color: var(--white);
    text-transform: uppercase;
  }
  .announcement .lead {
    display: block;
    font-weight: 400;
    font-size: 16px;
    letter-spacing: 0.3px;
  }
  .announcement .main {
    display: block;
    font-weight: 900;
    font-size: 22px;
    letter-spacing: 0.2px;
  }
  .front-cover .web-link {
    left: 60px; top: 522px;
    color: var(--white);
  }
  .web-link .domain-accent { color: var(--gold); }
</style>
</head>
<body>
  <main class="spread">
    <!-- back cover -->
    <section class="page back-cover">
      <svg class="page-art" width="440" height="600" viewBox="0 0 440 600" aria-hidden="false">
        <defs>
          <linearGradient id="livingRoomTone" x1="0" y1="0" x2="1" y2="1">
            <stop offset="0" stop-color="var(--photo-light-a)"/>
            <stop offset="1" stop-color="var(--photo-light-b)"/>
          </linearGradient>
        </defs>
        <path d="M0 0 H440 V60 Q220 110 0 190 Z" fill="var(--paper-light)"/>
        <path d="M0 190 Q220 110 440 60 V120 Q220 170 0 250 Z" fill="var(--paper-band)"/>
        <path role="img" aria-label="Photo of a bright modern living room with grey sofa, patterned rug and large windows"
              d="M0 250 Q220 170 440 120 V372 Q230 420 0 478 Z" fill="url(#livingRoomTone)"/>
      </svg>
      <p class="tagline">Don’t take our word for it!</p>
      <p class="web-link">
        <svg width="14" height="14" viewBox="0 0 14 14" aria-hidden="true">
          <g fill="none" stroke="currentColor" stroke-width="1.2">
            <circle cx="7" cy="7" r="6"/>
            <ellipse cx="7" cy="7" rx="2.6" ry="6"/>
            <line x1="1" y1="7" x2="13" y2="7"/>
          </g>
        </svg>
        www.brevanhomes.com
      </p>
    </section>

    <!-- front cover -->
    <section class="page front-cover">
      <svg class="page-art" width="440" height="600" viewBox="0 0 440 600">
        <defs>
          <linearGradient id="officeTone" x1="0" y1="0" x2="1" y2="1">
            <stop offset="0" stop-color="var(--photo-dark-a)"/>
            <stop offset="1" stop-color="var(--photo-dark-b)"/>
          </linearGradient>
        </defs>
        <path role="img" aria-label="Photo of the new office lounge with white sofa, abstract wall art and floor-to-ceiling windows"
              d="M0 196 Q200 160 330 150 L330 126 H440 V360 Q220 380 0 440 Z" fill="url(#officeTone)"/>
      </svg>
      <div class="headline-rank">
        <span class="rank-number">#1</span>
        <span class="rank-label">Local Indie<br>Real Estate<br>Company</span>
      </div>
      <div class="brand-name"><span class="brand-mark"></span>Brevan Homes</div>
      <p class="announcement">
        <span class="lead">Just opened our</span>
        <span class="main">Second Location</span>
      </p>
      <p class="web-link">
        <svg width="14" height="14" viewBox="0 0 14 14" aria-hidden="true">
          <g fill="none" stroke="currentColor" stroke-width="1.2">
            <circle cx="7" cy="7" r="6"/>
            <ellipse cx="7" cy="7" rx="2.6" ry="6"/>
            <line x1="1" y1="7" x2="13" y2="7"/>
          </g>
        </svg>
        <span>www.<span class="domain-accent">brevanhomes</span>.com</span>
      </p>
    </section>
  </main>
</body>
</html>
```